New Business Card Design Project

Hi there

Could you please make a design that is soft and appealing to people who would purchase gemstones, buy healing jewellery, seek counselling, may seek energy healing and/or learn English. Essentially I'm looking for something with a soft human design. Please incorporate the logo and select font that can be easily read and softer images in the background - but not too busy. I would like it double sided as well.

Optional: Elements could include gemstones, feathers, plants and images that are happy and calming.

Target Market(s)

People into alternative health, those from non-English speaking backgrounds, businesses

Contact Information for Business Card

Lena Whitford
Mobile: 0418 265 093, Facebook and Instagram Logos,
ABN: 61 472 185 034 (Australian Business Number - small at the bottom)

Requirements
Must have
• My project must have:
- Meadow Thread logo
- Symbols that represent the 4 main services: 1. Gemstones/jewellery, 2. counselling, 3. meditation/energy healing, 4. education
Nice to have
• Clear and easy to read.

```html
<!DOCTYPE html>
<html lang="en">
<head>
<meta charset="utf-8">
<title>Meadow Thread – Business Card</title>
<link href="https://fonts.googleapis.com/css2?family=Arimo:wght@400&display=swap" rel="stylesheet">
<style>
  :root {
    --backdrop: #b8b8b8;
    --paper: #ffffff;
    --teal: #05ada0;
    --green: #8cc63f;
    --ink: #2b2b2b;
    --social-a: #3b5998;
    --social-b: #d6336c;
  }
  * { margin: 0; padding: 0; box-sizing: border-box; }
  html, body {
    width: 1200px; height: 801px; overflow: hidden;
    background: var(--backdrop);
    font-family: "Arimo", Arial, sans-serif;
  }
  .card {
    position: absolute; top: 274px;
    width: 443px; height: 263px;
    background: var(--paper); overflow: hidden;
  }
  .card--front { left: 153px; }
  .card--back { left: 625px; }
  .card__waves { position: absolute; inset: 0; width: 443px; height: 263px; }
  .wave--teal { fill: var(--teal); }
  .wave--green { fill: var(--green); }

  .brand { position: absolute; text-align: center; width: 240px; }
  .brand__mark {
    display: block; margin: 0 auto;
    border: 2px solid var(--teal); border-radius: 50%;
  }
  .brand__name {
    display: block; color: var(--green); white-space: nowrap;
    font-size: 24px; line-height: 1; margin-top: 14px; letter-spacing: 0.5px;
  }
  .card--front .brand { left: 206px; top: 30px; }
  .card--front .brand__mark { width: 56px; height: 56px; }
  .card--back .brand { left: 189px; top: 31px; }
  .card--back .brand__mark { width: 50px; height: 50px; }
  .card--back .brand__name { font-size: 22px; margin-top: 12px; }

  .contact { position: absolute; left: 28px; top: 155px; }
  .contact__name { color: var(--teal); font-size: 20px; line-height: 24px; }
  .contact__phone { color: var(--ink); font-size: 16px; line-height: 20px; }
  .contact__abn { color: var(--ink); font-size: 12.5px; margin-top: 14px; }
  .contact__abn-label { color: var(--teal); }

  .social { position: absolute; left: 345px; top: 207px; display: flex; gap: 4px; }
  .social__dot { width: 20px; height: 20px; border-radius: 50%; }
  .social__dot--one { background: var(--social-a); }
  .social__dot--two { background: var(--social-b); }

  .services__title {
    position: absolute; left: 46px; top: 125px;
    color: var(--teal); font-size: 20px;
  }
  .service { position: absolute; top: 164px; width: 90px; text-align: center; }
  .service__art { width: 50px; height: 56px; margin: 0 auto; border-radius: 6px; }
  .service__label { color: var(--teal); font-size: 13px; margin-top: 6px; }
  .service--counselling { left: 25px; }
  .service--education { left: 110px; }
  .service--gemstones { left: 203px; }
  .service--meditation { left: 294px; }
  .service--counselling .service__art { background: linear-gradient(135deg, #d8eef0, #9fd3d6); }
  .service--education .service__art { background: linear-gradient(180deg, #9ccc5a, #3a8fc7, #e0559a); }
  .service--gemstones .service__art { background: linear-gradient(135deg, #d9822b, #e8e8e8, #6b3b8f); }
  .service--meditation .service__art { background: linear-gradient(180deg, #1fa79a, #22386b); }
</style>
</head>
<body>

<section class="card card--front">
  <svg class="card__waves" viewBox="0 0 443 263" aria-hidden="true">
    <path class="wave--teal" d="M0,0 H162 C130,20 95,25 70,40 C45,55 40,90 25,110 C15,122 5,128 0,134 Z"/>
    <path class="wave--green" d="M0,0 H110 C85,15 60,22 48,35 C35,50 30,75 18,85 C10,92 4,95 0,96 Z"/>
    <path class="wave--teal" d="M443,188 V263 H353 C370,250 390,245 405,238 C420,230 425,205 443,188 Z"/>
    <path class="wave--green" d="M443,210 V263 H375 C390,255 405,252 418,245 C430,238 432,222 443,210 Z"/>
  </svg>
  <div class="brand">
    <span class="brand__mark"></span>
    <span class="brand__name">Meadow Thread</span>
  </div>
  <div class="contact">
    <p class="contact__name">Lena Whitford</p>
    <p class="contact__phone">0418 265 093</p>
    <p class="contact__abn"><span class="contact__abn-label">ABN:</span> 61 472 185 034</p>
  </div>
  <div class="social">
    <span class="social__dot social__dot--one"></span>
    <span class="social__dot social__dot--two"></span>
  </div>
</section>

<section class="card card--back">
  <svg class="card__waves" viewBox="0 0 443 263" aria-hidden="true">
    <path class="wave--teal" d="M0,0 H162 C130,20 95,25 70,40 C45,55 40,90 25,110 C15,122 5,128 0,134 Z"/>
    <path class="wave--green" d="M0,0 H110 C85,15 60,22 48,35 C35,50 30,75 18,85 C10,92 4,95 0,96 Z"/>
    <path class="wave--teal" d="M443,188 V263 H353 C370,250 390,245 405,238 C420,230 425,205 443,188 Z"/>
    <path class="wave--green" d="M443,210 V263 H375 C390,255 405,252 418,245 C430,238 432,222 443,210 Z"/>
  </svg>
  <div class="brand">
    <span class="brand__mark"></span>
    <span class="brand__name">Meadow Thread</span>
  </div>
  <h2 class="services__title">Services</h2>
  <div class="service service--counselling">
    <div class="service__art" role="img" aria-label="Illustration of a head outline with gears for counselling"></div>
    <p class="service__label">Counselling</p>
  </div>
  <div class="service service--education">
    <div class="service__art" role="img" aria-label="Illustration of a stack of colourful books for education"></div>
    <p class="service__label">Education</p>
  </div>
  <div class="service service--gemstones">
    <div class="service__art" role="img" aria-label="Illustration of a faceted multicoloured gemstone"></div>
    <p class="service__label">Gemstones</p>
  </div>
  <div class="service service--meditation">
    <div class="service__art" role="img" aria-label="Illustration of a person sitting cross-legged in meditation"></div>
    <p class="service__label">Meditation</p>
  </div>
</section>

</body>
</html>
```